Skincare Label Design Completion

I am starting up a skincare business and need the graphic design completed.

A previous designer started the project but was not able to finish. The logo, BC, letterhead, With Comp & gift voucher is complete. The BC, Letterhead, WC & GV need change of contact details. The BC needs a bit of wording transferred from front to back to look 'cleaner'. There are 15 product labels which need finishing; one is 95% complete, two are 80% complete, 11 have the groundwork done, one is not started at all. Pantone has been used, this may need changing to CMYK as printers prefer this.

PRODUCT NAMES, PACKAGING AND SPECS: All attached.

LOGO SYMBOL: Is a simple wheat image. The .ai file it can be 'pulled' out of is attached.

FRENCH TRANSLATION: The French translations of product names are to feature within the label. (Please see attached pdf's; look for the colour "stripe".)

PRODUCT DIFFERENTIATION: A unique colour is to be introduced to each product label that corresponds to the botanical ingredients found within. Ie: a light green to match Aloe Vera. That secondary colour is to feature (minimally) within that label. In the attached pdf's it's been placed as a contrasting colour stripe. Other ideas welcome. :)

BOTANICAL IMAGES: THIS IS NON-ESSENTIAL - A simple botanical image could feature on each label to correspond to the product name, instead of the colour stripe. Ie: A rosehip and rose flower on the Rosehip, Lavender and Jojoba Facial Cleanser.

COLOUR MATCHING: Each of the "secondary" colours (please see Product Differentiation) need to match each other as well as the logo colours. Some of the products are designed as combo's; ie, cleanser and moisturiser combo's. The colours for these combo's need to work together. The previous designer did a pdf of suggested secondary colours (attached), however these are mostly not in sync with the businesses' approach of earthy/simple/easy to look at/purity. A friend did a pdf of earthy green secondary colours (pdf attached entitled "Sous_Ciel_Doux_FC") and did a few creative suggestions for the label. The font, colours and design he used in the TOP LEFT label is the one I prefer but please use your creative license should you feel a different font would look better.

- LABEL INFO -
95% COMPLETED LABEL: See pdf "Sous_Ciel_Doux_FC"; top left label, product "Aloe & Lemon Myrtle Facial Cleanser". This needs the light writing at the top changed to Pantone Black 5C, and a colour decided upon for the stripe (see below for more info). The product info needs to be checked for accuracy against the word doc I've provided. (Some info has changed.) Note: All of the cleansers, moisturisers, the spray mist and the hand cream use this exact same label as above, only with a different colour stripe for differentiation and wording / title changed.

80% COMPLETED LABELS: See pdf "Sous Ciel Doux_label_ v4-1":
1) "Clarifying Macadamia & Green Clay Facial Masque" needs a different colour stripe selected/inserted, the light writing above the logo needs changed to Pantone Black 5C, the font needs to be made the same as the above label "Aloe & Lemon Myrtle Facial Cleanser", and the product info updated as per the product info word doc attached.
2) "Cocoa Butter & Apricot Body Cream" need a different colour stripe selected/inserted, the font changed to the same as "Aloe & Lemon Myrtle Facial Cleanser" label, and the product info updated as per the word doc attached. The other labels on that pdf can be dismissed.

INCOMPLETE LABELS: As noted above, the "Aloe & Lemon Myrtle" cleanser label is exactly the same for 7 other products (cleansers, moisturisers, spray mist and hand cream). The "Sous_Ciel_Doux_FC" can be used as the basis for these. Each one needs a different colour stripe for differentiation chosen and inserted, and the light wording above the logo changed to Black 5C.

The products "Sandalwood & Shea Butter Facial Exfoliating Cream", "Jojoba, Ylang Ylang & Vanilla Facial Exfoliant" and "Sweet Orange & Lavender Hand & Foot Scrub" all use exactly the same labels (one for jar, one for lid) as the Clarifying Macadamia & Green Clay masque. So you should be able to replicate this label for the other products. Each of these need the light writing above the logo changed to Black 5C and the colour stripes selected/inserted.

In the pdf "Sous Ciel Doux_label_ v4-1" the the 250mL bottle label has been completed. However that particular product was deleted. So using that label you can "pull out" the discontinued label wording and colour stripe, and replace it with the "Rosehip Body Lotion" label info. This also needs the light writing above the logo to be replaced with Pantone Black 5C, the colour stripe decided upon/inserted and the font to match with the above.

Only the lip balm has absolutely no work done on it. This will be just one small rectangular label.

Please note: this is not a re-branding so please stay true to the logo colours of Pantone 2717C, 4685C and Black 5C for the majority of the label. Secondary colour use is fine to match the botanicals.

Thank you so much in advance for your designs! :)

Maren.

Target Market(s)

Women aged 16 - 65+
Environmentally aware
Natural over chemical
Will spend a higher amount for a quality product
Women who want the best

Industry/Entity Type

Graphic Design

Font styles to use
Other font styles liked:
• Attached pdf "Sous_Ciel_Doux_FC" - top left label

Requirements
Must have
• Simple, clean lines, purity, natural / earthy colours.
• Secondary colours carefully chosen to reflect the botanical ingredients and to match the logo colours and each other.
• French translations on labels.
• LABELS MUST STAY WITH COLOURS MENTIONED IN BRIEF: PANTONE 2717C, 4685C, BLACK 5C - This is not a re-branding so please don't stray from using these colours for the majority of the label. (For secondary colour use to match botanicals, please use your creative license.)
Nice to have
• Botanical image on each label - non-essential
Should not have
• Nothing modern, harsh, stark or intense

```html
<!DOCTYPE html>
<html lang="en">
<head>
<meta charset="utf-8">
<title>Sous Ciel Doux – Business Card</title>
<link rel="stylesheet" href="https://fonts.googleapis.com/css2?family=Questrial&family=Raleway:wght@700&display=swap">
<style>
  :root {
    --sky: #b6e0fc;
    --peach: #f1d7c3;
    --stone: #7d736a;
    --stone-light: #938a80;
    --logo-grey: #77736a;
    --cream: #f6efe7;
    --page: #ffffff;
  }
  * { margin: 0; padding: 0; box-sizing: border-box; }
  html, body {
    width: 1200px; height: 1067px; overflow: hidden;
    background: var(--page);
    font-family: "Questrial", "Century Gothic", sans-serif;
  }
  .canvas { position: relative; width: 1200px; height: 1067px; }

  .card {
    position: absolute; left: 303px; width: 597px; height: 332px;
    border-radius: 18px; overflow: hidden;
  }
  .card--front { top: 167px; background: var(--sky); }
  .card--back  { top: 555px; background: var(--stone); }

  /* front */
  .wheat-side {
    position: absolute; top: 0; height: 100%; width: 62px;
    background: linear-gradient(180deg, rgba(241,215,195,.35), rgba(241,215,195,.15));
  }
  .wheat-side--left { left: 0; }
  .wheat-side--right { right: 0; }
  .frame { position: absolute; left: 59px; top: 64px; width: 477px; height: 205px; }
  .wheat-inner {
    position: absolute; left: 66px; top: 86px; width: 56px; height: 160px;
    background: linear-gradient(180deg, rgba(241,215,195,.55), rgba(241,215,195,.2));
    border-radius: 28px 28px 4px 4px;
  }
  .brand-name {
    position: absolute; left: 0; width: 100%; top: 112px; padding-left: 36px;
    text-align: center; font-size: 46px; color: var(--logo-grey); letter-spacing: 1px;
  }
  .brand-tagline {
    position: absolute; left: 0; width: 100%; top: 191px; padding-left: 36px;
    text-align: center; font-size: 14px; letter-spacing: 5px; color: var(--peach);
  }

  /* back */
  .wheat-sprig {
    position: absolute; left: 318px; top: 0; width: 279px; height: 100%;
    background: linear-gradient(200deg, rgba(190,180,168,.45), rgba(190,180,168,.12) 70%);
    clip-path: polygon(8% 0, 40% 0, 100% 60%, 100% 100%, 55% 100%, 25% 40%);
  }
  .holder-name {
    position: absolute; left: 43px; top: 54px;
    font-size: 20px; letter-spacing: 3px; color: var(--sky);
  }
  .contact { position: absolute; left: 43px; top: 128px; list-style: none;
    font-size: 15px; letter-spacing: 1.5px; color: var(--cream); line-height: 23px; }
  .contact .label { display: inline-block; width: 26px; }
  .contact .web { color: var(--sky); font-weight: bold; }
  .offer { position: absolute; left: 43px; top: 263px; width: 350px; text-align: center; color: var(--cream); }
  .offer__main { font-family: "Raleway", "Century Gothic", sans-serif; font-weight: 700; font-size: 16px; }
  .offer__amp { font-size: 22px; font-weight: 400; font-family: "Questrial", sans-serif; }
  .offer__sub { font-size: 13px; letter-spacing: .5px; margin-top: 1px; }
</style>
</head>
<body>
<main class="canvas">
  <section class="card card--front">
    <div class="wheat-side wheat-side--left" role="img" aria-label="Faint wheat stalk illustration"></div>
    <div class="wheat-side wheat-side--right" role="img" aria-label="Faint wheat stalk illustration"></div>
    <svg class="frame" viewBox="0 0 477 205" aria-hidden="true">
      <rect x="1.5" y="1.5" width="474" height="202" rx="6" fill="none" stroke="#f1d7c3" stroke-width="3"/>
      <rect x="9" y="9" width="459" height="187" rx="3" fill="none" stroke="#f1d7c3" stroke-width="1.5"/>
    </svg>
    <div class="wheat-inner" role="img" aria-label="Wheat ear illustration"></div>
    <h1 class="brand-name">Sous Ciel Doux</h1>
    <p class="brand-tagline">UNDER A SOFT SKY</p>
  </section>

  <section class="card card--back">
    <div class="wheat-sprig" role="img" aria-label="Wheat sprig illustration"></div>
    <h2 class="holder-name">MAREN ALDER</h2>
    <ul class="contact">
      <li><span class="label">M:</span>0412 555 208</li>
      <li><span class="label">E:</span>maren@souscieldouxonline.com</li>
      <li><span class="label">W:</span><span class="web">www.souscieldouxonline.com</span></li>
    </ul>
    <div class="offer">
      <p class="offer__main">BOTANICAL FACE <span class="offer__amp">&amp;</span> BODY PRODUCTS</p>
      <p class="offer__sub">HAND-MADE WITH PASSION &amp; CONSCIENCE</p>
    </div>
  </section>
</main>
</body>
</html>
```